Flyer-Design für Zauber-Projekt
Sehr netter und kreativer Kontakt, alle Änderungswünsche wurden kurzfristig umgesetzt, vielen Dank! Meine Flyer gefallen mir super gut! :-)
Zielgruppe
Ich bin Zauberkünstlerin und auf der Suche nach Flyern für ein spezielles Projekt. Dabei handelt es sich um das vermutlich kleinste Zaubertheater der Welt- eine Art Box, die sehr vintage aussieht (wie ein Relikt aus dem 19. Jahrhundert). Wirft man Geld in den Münzschlitz, öffnen sich die Türen des 'Pling-E-Tor' und ich unterhalte das Publikum mit erstaunlichen Zaubereien :-) Zielgruppe sind Firmen, die eine Kunden- und Gäste-Unterhaltung für ihre Messe- oder andere Kundenveranstaltungen (z.B. Tag der offenen Türe, Jubiläen, ...) suchen, oder Kulturschaffende wie Varietès, Theater, Museen etc, in denen der Pling-E-Tor im Wartebereich stehen könnte.
Aufgabenstellung
Der Flyer sollte gerne im 'Vintage-Style' sein, um die 'Magie' des Pling-e-Tor zu transportieren und dennoch ansprechend auf Firmen wirken, d.h. eine Mischung aus Vintage und 'Modern-Professionell' wäre ideal. Weiteres Bildmaterial stelle ich gerne zur Verfügung. Als Schriftart finde ich 'Chopin' oder 'Rochester' sehr schön, vielleicht für die Überschriften?

```html
<!DOCTYPE html>
<html lang="de">
<head>
<meta charset="utf-8">
<title>Pling-E-Tor – Flyer</title>
<link rel="stylesheet" href="https://fonts.googleapis.com/css2?family=Pinyon+Script&family=Sorts+Mill+Goudy&display=swap">
<style>
  :root {
    --bg-deep: #4a1019;
    --bg-mid: #66202b;
    --bg-light: #742a35;
    --ink: #f6efe9;
    --photo-red: #8c1a26;
    --photo-grey: #7d8189;
    --photo-gold: #b8913f;
  }
  * { margin: 0; padding: 0; box-sizing: border-box; }
  html, body { width: 1200px; height: 1199px; overflow: hidden; }
  body {
    background: radial-gradient(ellipse at 50% 55%, var(--bg-light) 0%, var(--bg-mid) 45%, var(--bg-deep) 100%);
    color: var(--ink);
    font-family: "Sorts Mill Goudy", Georgia, serif;
  }
  .flyer { position: relative; width: 1200px; height: 1199px; }
  .script { font-family: "Pinyon Script", cursive; font-weight: 400; }
  .body-text {
    font-size: 23.5px;
    line-height: 34px;
    text-align: justify;
    hyphens: auto;
  }
  .intro { position: absolute; left: 77px; top: 48px; width: 392px; }
  .intro h2 { font-size: 48px; line-height: 60px; margin-bottom: 2px; }
  .hero-photo {
    position: absolute; left: 590px; top: 47px; width: 534px; height: 463px;
    background: linear-gradient(180deg, var(--photo-grey) 0%, #5d5f66 45%, var(--photo-red) 75%, #5e1018 100%);
    border-left: 14px solid var(--photo-gold);
    border-right: 14px solid var(--photo-gold);
  }
  .brand {
    position: absolute; left: 77px; top: 570px;
    font-size: 50px; line-height: 60px; letter-spacing: 1px;
  }
  .contact { position: absolute; left: 77px; top: 688px; }
  .contact .greeting { font-size: 31px; line-height: 34px; margin-bottom: 22px; }
  .contact address { font-style: normal; font-size: 23.5px; line-height: 34px; }
  .contact .spacer { height: 34px; }
  .booking { position: absolute; left: 675px; top: 567px; width: 396px; }
  .booking h2 { font-size: 52px; line-height: 54px; margin-bottom: 6px; }
  .tagline {
    position: absolute; left: 0; right: 0; top: 1078px;
    text-align: center; font-size: 72px; line-height: 90px;
  }
</style>
</head>
<body>
<main class="flyer">
  <section class="intro">
    <h2 class="script">Ein Blickfang</h2>
    <p class="body-text">Mit viel kreativem Herzblut in Eigenregie gestaltet, bereichert der Pling-E-Tor als optischer Blickfang jede Veranstaltung. Die geheimnisvolle Lady Rosalie, die ihr Publikum mit charmant-humorvoller Zauberei an ihren Sinnen zweifeln lässt, vollendet den Pling-E-Tor zu einem faszinierenden Gesamtkunstwerk.</p>
  </section>

  <div class="hero-photo" role="img" aria-label="Foto: Zauberkünstlerin in schwarzem Kleid im goldgerahmten Zaubertheater mit rotem Samttisch"></div>

  <div class="brand">Pling-E-Tor</div>

  <section class="contact">
    <p class="greeting">Ich freue mich<br>auf Ihre Nachricht</p>
    <address>
      Petra Kux<br>
      Lindenhofweg 7<br>
      72108 Falkenau
      <div class="spacer"></div>
      Rosalie@pling-e-tor.de<br>
      www. pling-e-tor.de<br>
      +49 151 2340987
    </address>
  </section>

  <section class="booking">
    <h2 class="script">Werbung, die Ihre<br>Kunden verzaubert</h2>
    <p class="body-text">Buchen Sie den Pling-E-Tor für Ihre Messe oder Veranstaltung und stellen Sie eine „magische“ Verbindung zu Ihrer Firma her. Kombinieren Sie den Pling-E-Tor mit Ihren Aufstellern, Beachflags oder Bannern - eine zauberhafte Verknüpfung zwischen Ihrer Firma und dem Publikum ist garantiert! Gerne beraten wir Sie über geeignetes Werbematerial.</p>
  </section>

  <p class="tagline script">Türen auf - lassen Sie sich verzaubern!</p>
</main>
</body>
</html>
```